Creative and elegant Brochure Design Project

Graceful Bidwell, a online platform to design and sen out online invitations, track RSVP, create seating charts, place cards, thank you cards as well as a gift registry.
Should have clean and elegant outer sides, with more informative inner sides, like features, or pricing, or other information that can be found both on the website and the articles attached.
can include something like: Graceful Bidwell is more than just a way to create simple elegant invitations. It is a whole suite of event management tools.
UNIQUE EDITABLE DESIGNS
INSTANT RSVP'S
LAST MINUTE INVITES
GUEST MANAGEMENT TOOLS
AUTOMATED SEATING CHARTS AND PLACE CARDS
CALENDAR INTEGRATION AND MESSAGING
AUTOMATED THANK YOU CARDS
GIFT REGISTRY
OPTIONAL PRINTED POSTCARDS
Industry/Entity Type
Event Planning
Colors
Designer to choose colors to be used in the design.
Look and feel
Each slider illustrates characteristics of the customer's brand and the style your logo design should communicate.

```html
<!DOCTYPE html>
<html lang="en">
<head>
<meta charset="utf-8">
<title>Graceful Bidwell — Brochure</title>
<link href="https://fonts.googleapis.com/css2?family=Cinzel:wght@400;500&family=Montserrat:wght@300;400;600;700&display=swap" rel="stylesheet">
<style>
  :root{
    --backdrop:#8f8c89;
    --paper:#f5f5f4;
    --rule:#dcdcdb;
    --gold:#b09a5b;
    --ink:#3a3a3a;
    --ink-soft:#555;
  }
  *{box-sizing:border-box;margin:0;padding:0}
  html,body{width:1200px;height:1200px;overflow:hidden;background:var(--backdrop)}
  body{position:relative;font-family:'Montserrat',sans-serif;color:var(--ink)}
  .sheet{position:absolute;top:240px;width:575px;height:720px;background:var(--paper);box-shadow:0 3px 12px rgba(0,0,0,.22)}
  .sheet--outer{left:17px}
  .sheet--inner{left:608px}
  .panel{position:relative;height:240px;border-bottom:1px solid var(--rule);overflow:hidden}
  .panel:last-child{border-bottom:none}
  .gold-band{height:26px;background:linear-gradient(90deg,#a68f50,#bca66a,#a68f50)}
  .placeholder{position:absolute;border-radius:2px}

  /* outer: cover panel */
  .cover-title{position:absolute;left:10px;width:320px;top:62px;text-align:center;font-family:'Cinzel',serif;font-weight:400;color:var(--gold);font-size:22px;line-height:30px;letter-spacing:.5px}
  .brand{position:absolute;left:10px;width:320px;top:138px;display:flex;justify-content:center;align-items:center;gap:8px;font-weight:400;color:var(--gold);font-size:11.5px;letter-spacing:1px}
  .brand-dot{width:9px;height:9px;border-radius:50%;background:var(--gold)}
  .envelope-dark{left:350px;top:40px;width:150px;height:135px;background:linear-gradient(160deg,#c9ad62 0%,#c9ad62 35%,#2f2f31 36%,#1f1f21 100%)}
  .features{position:absolute;left:0;right:0;top:192px;text-align:center;font-family:'Cinzel',serif;font-size:9px;line-height:11.5px;color:var(--ink);letter-spacing:.3px}

  /* outer: contact panel */
  .envelope-mauve{left:55px;top:40px;width:165px;height:150px;background:linear-gradient(160deg,#d9b95a 0%,#d9b95a 38%,#7e5e5a 39%,#6d5250 100%)}
  .contact{position:absolute;left:290px;width:230px;top:72px;text-align:center;font-size:9px;line-height:11.5px;color:var(--ink-soft)}
  .contact .site{font-weight:600;font-size:11px;color:var(--ink)}
  .social{position:absolute;left:348px;top:150px;display:flex;gap:10px}
  .social span{width:24px;height:24px;border-radius:50%;background:var(--gold)}

  /* outer: gallery panel */
  .photo-strip{position:absolute;top:38px;left:45px;display:flex;gap:2px}
  .photo-strip .placeholder{position:static;width:160px;height:150px;background:linear-gradient(135deg,#ece5de,#d8c9c0 60%,#e7c79c)}

  /* inner: story panel */
  .story{position:absolute;left:28px;top:38px;width:320px;font-size:7.5px;line-height:9.3px;color:var(--ink-soft)}
  .story p{margin-bottom:3px}
  .envelope-open{left:362px;top:52px;width:190px;height:140px;background:linear-gradient(150deg,#9c8843 0%,#a08c4a 30%,#eeeeee 31%,#e2e2e2 100%)}

  /* inner: tablet panel */
  .wood{left:0;top:0;width:100%;height:100%;border-radius:0;background:linear-gradient(90deg,#b8ada2,#c9bfb5 50%,#b5aa9f)}
  .tablet{position:absolute;left:30px;top:12px;width:410px;height:216px;border-radius:12px;background:#e3e3e3;box-shadow:0 2px 8px rgba(0,0,0,.25)}
  .tablet-screen{position:absolute;left:20px;top:12px;right:12px;bottom:12px;background:#fafafa;padding:6px 8px;font-size:7.3px;line-height:9px;color:var(--ink-soft);text-align:justify}
  .tablet-screen p{margin-bottom:2.5px}
  .blush-envelope{left:458px;top:12px;width:100px;height:85px;background:linear-gradient(180deg,#d4958a,#e9c7c0)}
  .tulips{left:468px;top:108px;width:80px;height:118px;background:linear-gradient(180deg,#f1f1ee,#c9d4b3)}

  /* inner: services panel */
  .columns{position:absolute;left:28px;top:24px;display:flex;gap:18px}
  .col{font-size:7.5px;line-height:9.4px;color:var(--ink-soft);text-align:justify}
  .col--registry{width:200px}
  .col--print{width:152px}
  .col h3{font-size:8.6px;font-weight:700;color:var(--ink);letter-spacing:.3px;margin-top:4px}
  .col p{margin-bottom:3px}
  .col b{color:var(--ink)}
  .screens{left:412px;top:14px;width:143px;height:180px;background:linear-gradient(180deg,#dedede,#cfcfcf)}
  .closing{position:absolute;left:0;right:0;top:216px;text-align:center;font-size:7.8px;color:var(--ink)}
</style>
</head>
<body>

<section class="sheet sheet--outer">
  <div class="panel panel--cover">
    <div class="gold-band"></div>
    <h1 class="cover-title">Just the Joy.<br>None of the Stress.</h1>
    <div class="brand">GRACEFUL BIDWELL <span class="brand-dot"></span></div>
    <div class="placeholder envelope-dark" role="img" aria-label="Photograph of a black envelope with a gold foil liner"></div>
    <p class="features">Unique Editable Designs · Instant RSVPs · Last Minute Invites · Guest Management Tools<br>Automated Seating Charts and Place Cards · Calendar Integration and Messaging<br>Automated Thank You Cards · Gift Registry · Optional Printed Postcards</p>
  </div>
  <div class="panel panel--contact">
    <div class="placeholder envelope-mauve" role="img" aria-label="Photograph of a mauve envelope with a gold liner on a light desk"></div>
    <div class="contact">
      <div class="site">gracefulbidwell.com</div>
      P. O. Box 480 Millbrook, NJ 07940<br>
      Customer service +1 800 555 0142<br>
      Mon - Thu 09:00 - 20:00<br>
      Fri &amp; Sun 09:00 - 12:00
    </div>
    <div class="social" aria-label="Social channels"><span></span><span></span><span></span><span></span></div>
  </div>
  <div class="panel panel--gallery">
    <div class="photo-strip">
      <div class="placeholder" role="img" aria-label="Photograph of blush wedding stationery with gold accents and flowers"></div>
      <div class="placeholder" role="img" aria-label="Photograph of a table number card and invitations with flowers"></div>
      <div class="placeholder" role="img" aria-label="Photograph of an invitation suite on blush paper"></div>
    </div>
  </div>
</section>

<section class="sheet sheet--inner">
  <div class="panel panel--story">
    <div class="gold-band"></div>
    <div class="story">
      <p>The glass breaks, the music plays and the crowd surges forward to say mazel tov to the chassan and kallah. The bar mitzvah bachur finishes his drasha to the acclaim of all the guests. Simchas are supposed to be happy occasions and we wait for the beautiful highlights and emotional moments.</p>
      <p>But the actual experience can be nerve-wracking and frustrating, when you're trying to juggle all of the tasks needed to actually get the simcha off the ground, including inviting guests, seating them, and making sure you'll thank them afterwards.</p>
      <p>You need to worry about getting the text you'll be using to a print shop and aligning labels on your home printer.</p>
      <p>You need to deal with mailing hassles: stamping and licking envelopes, getting everything to the post office.</p>
      <p>But even then, you're not done. You need to wait for the snail mail to reach your guests' homes and for the RSVP cards to find their way back to you. And then comes the mind-numbing chore of opening each envelope, deciphering the handwriting, and marking down the guests' choices.</p>
      <p>After that, you'll need to get out your seating chart, find your list of attendees, and start figuring out, painstakingly, where everyone goes.</p>
    </div>
    <div class="placeholder envelope-open" role="img" aria-label="Photograph of an open envelope with gold liner, rings and a branded card with flowers"></div>
  </div>
  <div class="panel panel--tablet">
    <div class="placeholder wood" role="img" aria-label="Photograph of a light wooden tabletop with petals"></div>
    <div class="tablet">
      <div class="tablet-screen">
        <p>At one time, planning a Jewish wedding meant sending invitations out of town on a donkey-driven wagon. But today it's possible to get everything you need done easily, all in one place, with <b>Graceful Bidwell's</b> innovative service.</p>
        <p>Your entire guest list gets entered online, using a simple interface. Choose from numerous uniquely designed and editable invitations and send them out by simply pressing <b>Enter</b> on your keyboard.</p>
        <p>Your guests receive their invitations immediately and can't misplace them – and can RSVP easily from their own computers.</p>
        <p>Using your guest list, <b>Graceful Bidwell</b> lets you arrange seating charts, create place cards and generate thank-you cards for gifts at the click of a button. You won't be juggling reams of papers and numerous lists; everything is right there online. No one is left out; no one is forgotten; no one is hurt because they haven't received an invitation, a place setting, or a thank you card.</p>
        <p>And that also means your event is a pleasure for your guests. Rather than a pile of invitations sitting on their kitchen table or hung on their fridge, they can receive and review your invitation with no hassle and it's always available electronically. They won't forget to attend your events or be unable to remember where they will be taking place.</p>
      </div>
    </div>
    <div class="placeholder blush-envelope" role="img" aria-label="Photograph of a blush patterned envelope"></div>
    <div class="placeholder tulips" role="img" aria-label="Photograph of white tulips"></div>
  </div>
  <div class="panel panel--services">
    <div class="columns">
      <div class="col col--registry">
        <h3>ONLINE GIFT REGISTRY</h3>
        <p>When guests RSVP for your event, they can instantly choose their gift, whether they're able to attend or not, with the logistics taken care of.</p>
        <h3>SUBSTANTIAL SAVINGS</h3>
        <p><b>Graceful Bidwell</b> gives you all the elegance and exclusive designs of incredibly expensive printed invitations at much lower cost – but with all of the control that printed invitations never can. Use our custom features for smaller events, like bar and bat mitzvahs, baby birth events and engagements, to create a smoother experience and a better and bigger gift registry.</p>
      </div>
      <div class="col col--print">
        <h3>OPTIONAL PRINTING SERVICE</h3>
        <p>When you want to use print invitations for all of your guests, <b>Graceful Bidwell's</b> RSVP service gives you seating chart creation, place card automation and thank you card production. And because the RSVPing happens online, you'll know who is coming right away, and your seating charts and place cards can be made right from that list.</p>
        <p>If most of your guests are fine with receiving digital invitations but a few would really appreciate a paper invitation, we can print them for you.</p>
      </div>
    </div>
    <div class="placeholder screens" role="img" aria-label="Screenshots of the online guest management dashboard"></div>
    <p class="closing">The modern age has arrived, and it will make your simcha a truly happy one!</p>
  </div>
</section>

</body>
</html>
```